Monthly Planner & To Do List on dry erase magnetic whiteboard

I'm after 2 x designs for magnetic whiteboards.
1. 17 x 13 inches is a monthly planner. Dates and month can be written in each month and then wiped off and re-written for the next month.
2. 6 x 4 inches - to do list however I don't want this to say To Do on it but will have lines to write on and possibly bullet points to check off.
I have attached below samples of other products (the ones I like the most are the first two - 9.19.52 and 9.20.34). I actually don't like the design of the others but just show them here as an example for layout purposes.
I want something that is modern, slick, simple yet stylish which is what my brand is representative of - smart, modern, organised. It will be printed onto a white board and I only want the print to be in black, no grey shading. I need a more modern font and don't like any of the swirly parts. Just clean and simple but slick.
I would like the size of the day squares to be as large as possible to fit writing in them and also for a section somewhere on the page for additional notes.

Requirements
Should not have
• Old style fonts, cartoon style or childish.

```html
<!DOCTYPE html>
<html lang="en">
<head>
<meta charset="UTF-8">
<title>Monthly Planner and To Do List Boards</title>
<link href="https://fonts.googleapis.com/css2?family=Josefin+Sans:wght@300;400;600&family=Montserrat:wght@400;700&family=Playfair+Display:wght@700&display=swap" rel="stylesheet">
<style>
  :root {
    --ink: #0f3649;
    --white: #ffffff;
    --rule: #3a3a3a;
    --dot: #e2e2e2;
    --day-light: #ececec;
    --day-dark: #dcdcdc;
    --notes-body: #e4e4e4;
    --notes-line: #b9b9b9;
    --label: #3b3b3b;
    --bg-center: #f2f2f2;
    --bg-edge: #8f8f8f;
  }
  * { margin: 0; padding: 0; box-sizing: border-box; }
  html, body { width: 918px; height: 1200px; overflow: hidden; }
  body {
    position: relative;
    background: radial-gradient(ellipse 70% 60% at 50% 50%, var(--bg-center), var(--bg-edge));
    font-family: "Josefin Sans", sans-serif;
  }
  .side-label {
    position: absolute;
    font-family: "Montserrat", sans-serif;
    font-weight: 700;
    font-size: 25px;
    letter-spacing: 1px;
    color: var(--label);
    white-space: nowrap;
    transform: translate(-50%, -50%) rotate(-90deg);
  }
  .side-label--planner { left: 70px; top: 353px; }
  .side-label--todo { left: 70px; top: 946px; }

  .board { position: absolute; background: var(--white); }
  .board__footer { position: absolute; left: 0; right: 0; bottom: 0; background: var(--ink); }

  /* Monthly planner */
  .planner { left: 102px; top: 62px; width: 724px; height: 552px; }
  .planner__header { position: absolute; left: 0; top: 0; width: 100%; height: 90px; background: var(--ink); color: var(--white); }
  .planner__month-of { position: absolute; left: 52px; top: 56px; font-size: 17px; font-weight: 300; letter-spacing: 0.5px; }
  .planner__title { position: absolute; right: 46px; top: 22px; font-size: 57px; line-height: 1; letter-spacing: 1px; }
  .planner__month { font-weight: 400; }
  .planner__year { font-weight: 300; margin-left: 6px; }
  .planner__footer { height: 12px; }

  .weekdays { position: absolute; left: 49px; top: 100px; width: 499px; height: 31px; display: flex; }
  .weekday {
    flex: 1; display: flex; align-items: center; justify-content: center;
    font-family: "Montserrat", sans-serif; font-size: 9.5px; color: #333;
    background: var(--day-light);
  }
  .weekday:nth-child(even) { background: var(--day-dark); }
  .calendar-grid { position: absolute; left: 49px; top: 132px; }

  .notes { position: absolute; left: 566px; top: 100px; width: 112px; height: 420px; background: var(--notes-body); }
  .notes__title {
    height: 28px; background: var(--ink); color: var(--white);
    font-size: 14.5px; font-weight: 600; letter-spacing: 0.5px;
    padding: 7px 0 0 13px;
  }
  .notes__lines { position: absolute; left: 10px; top: 0; }

  /* To do list */
  .todo { left: 98px; top: 640px; width: 725px; height: 484px; }
  .todo__header {
    position: absolute; left: 0; top: 0; width: 100%; height: 109px; background: var(--ink);
    color: var(--white); display: flex; align-items: center; justify-content: center;
  }
  .todo__title { font-size: 49px; font-weight: 300; letter-spacing: 1px; padding-top: 10px; }
  .todo__list { position: absolute; left: 0; top: 0; }
  .todo__number { font-family: "Playfair Display", serif; font-weight: 700; font-size: 27px; fill: #1a1a1a; }
  .todo__footer { height: 14px; }
</style>
</head>
<body>
  <div class="side-label side-label--planner">MONTHLY PLANNER</div>
  <div class="side-label side-label--todo">TO DO LIST</div>

  <section class="board planner">
    <header class="planner__header">
      <span class="planner__month-of">MONTH OF</span>
      <h1 class="planner__title"><span class="planner__month">JUNE</span><span class="planner__year">2018</span></h1>
    </header>

    <div class="weekdays">
      <div class="weekday">SUNDAY</div>
      <div class="weekday">MONDAY</div>
      <div class="weekday">TUESDAY</div>
      <div class="weekday">WEDNESDAY</div>
      <div class="weekday">THURSDAY</div>
      <div class="weekday">FRIDAY</div>
      <div class="weekday">SATURDAY</div>
    </div>

    <svg class="calendar-grid" width="500" height="390" viewBox="0 0 500 390">
      <g fill="var(--dot)">
        <circle cx="11" cy="11" r="8"/><circle cx="82" cy="11" r="8"/><circle cx="153.6" cy="11" r="8"/><circle cx="225" cy="11" r="8"/><circle cx="296" cy="11" r="8"/><circle cx="367.5" cy="11" r="8"/><circle cx="439" cy="11" r="8"/>
        <circle cx="11" cy="89" r="8"/><circle cx="82" cy="89" r="8"/><circle cx="153.6" cy="89" r="8"/><circle cx="225" cy="89" r="8"/><circle cx="296" cy="89" r="8"/><circle cx="367.5" cy="89" r="8"/><circle cx="439" cy="89" r="8"/>
        <circle cx="11" cy="166" r="8"/><circle cx="82" cy="166" r="8"/><circle cx="153.6" cy="166" r="8"/><circle cx="225" cy="166" r="8"/><circle cx="296" cy="166" r="8"/><circle cx="367.5" cy="166" r="8"/><circle cx="439" cy="166" r="8"/>
        <circle cx="11" cy="244" r="8"/><circle cx="82" cy="244" r="8"/><circle cx="153.6" cy="244" r="8"/><circle cx="225" cy="244" r="8"/><circle cx="296" cy="244" r="8"/><circle cx="367.5" cy="244" r="8"/><circle cx="439" cy="244" r="8"/>
        <circle cx="11" cy="321" r="8"/><circle cx="82" cy="321" r="8"/><circle cx="153.6" cy="321" r="8"/><circle cx="225" cy="321" r="8"/><circle cx="296" cy="321" r="8"/><circle cx="367.5" cy="321" r="8"/><circle cx="439" cy="321" r="8"/>
      </g>
      <g stroke="var(--rule)" stroke-width="1" fill="none">
        <rect x="0.5" y="0.5" width="499" height="388"/>
        <line x1="71.8" y1="0" x2="71.8" y2="389"/>
        <line x1="143.1" y1="0" x2="143.1" y2="389"/>
        <line x1="214.4" y1="0" x2="214.4" y2="389"/>
        <line x1="285.7" y1="0" x2="285.7" y2="389"/>
        <line x1="357" y1="0" x2="357" y2="389"/>
        <line x1="428.3" y1="0" x2="428.3" y2="389"/>
        <line x1="0" y1="78" x2="500" y2="78"/>
        <line x1="0" y1="155.5" x2="500" y2="155.5"/>
        <line x1="0" y1="233" x2="500" y2="233"/>
        <line x1="0" y1="310.5" x2="500" y2="310.5"/>
      </g>
    </svg>

    <aside class="notes">
      <div class="notes__title">NOTES</div>
      <svg class="notes__lines" width="94" height="420" viewBox="0 0 94 420">
        <g stroke="var(--notes-line)" stroke-width="0.8">
          <line x1="0" y1="45" x2="94" y2="45"/><line x1="0" y1="63.3" x2="94" y2="63.3"/><line x1="0" y1="81.6" x2="94" y2="81.6"/><line x1="0" y1="99.9" x2="94" y2="99.9"/>
          <line x1="0" y1="118.2" x2="94" y2="118.2"/><line x1="0" y1="136.5" x2="94" y2="136.5"/><line x1="0" y1="154.8" x2="94" y2="154.8"/><line x1="0" y1="173.1" x2="94" y2="173.1"/>
          <line x1="0" y1="191.4" x2="94" y2="191.4"/><line x1="0" y1="209.7" x2="94" y2="209.7"/><line x1="0" y1="228" x2="94" y2="228"/><line x1="0" y1="246.3" x2="94" y2="246.3"/>
          <line x1="0" y1="264.6" x2="94" y2="264.6"/><line x1="0" y1="282.9" x2="94" y2="282.9"/><line x1="0" y1="301.2" x2="94" y2="301.2"/><line x1="0" y1="319.5" x2="94" y2="319.5"/>
          <line x1="0" y1="337.8" x2="94" y2="337.8"/><line x1="0" y1="356.1" x2="94" y2="356.1"/><line x1="0" y1="374.4" x2="94" y2="374.4"/><line x1="0" y1="392.7" x2="94" y2="392.7"/>
        </g>
      </svg>
    </aside>

    <div class="board__footer planner__footer"></div>
  </section>

  <section class="board todo">
    <header class="todo__header">
      <h2 class="todo__title">THINGS TO DO TODAY</h2>
    </header>

    <svg class="todo__list" width="725" height="484" viewBox="0 0 725 484">
      <g fill="var(--dot)">
        <circle cx="64" cy="146" r="17"/><circle cx="64" cy="201" r="17"/><circle cx="65" cy="253" r="17"/>
        <circle cx="65" cy="309" r="17"/><circle cx="66" cy="358" r="17"/><circle cx="66" cy="408" r="17"/>
      </g>
      <g class="todo__number">
        <text x="94" y="158">1</text><text x="95" y="210">2</text><text x="95" y="262">3</text>
        <text x="94" y="314">4</text><text x="95" y="366">5</text><text x="95" y="418">6</text>
      </g>
      <g stroke="var(--rule)" stroke-width="1">
        <line x1="112" y1="158.5" x2="692" y2="158.5"/><line x1="112" y1="210.5" x2="692" y2="210.5"/><line x1="112" y1="262.5" x2="692" y2="262.5"/>
        <line x1="112" y1="314.5" x2="692" y2="314.5"/><line x1="112" y1="366.5" x2="692" y2="366.5"/><line x1="112" y1="418.5" x2="692" y2="418.5"/>
      </g>
    </svg>

    <div class="board__footer todo__footer"></div>
  </section>
</body>
</html>
```